Children's writer business card design

I write children's mystery and adventure books for 9-12 year olds. My logo is a small robin redbreast bird which I will appear on all my commercial stationery and websites. I have a 'silhouette' of a bird on the mock up on your site and I like this, although your designers might make it look even better. The bird is non-negotiable!

When I tried to do the back of the card I got a hallmark. I don't like this.

I would like the card to be modern, 'clean' and striking. Not too much colour. Definitely the red for the bird so it really stands out.

Target Market(s)

parents and grandparents of children 9-12 years old, booksellers, teachers

Industry/Entity Type

Business

Contact Information for Business Card

I have created a rough design using Cardloft which I hope you can access as this contains all of the information I want on my card.
The front has the following:
Mabel Frandsen
Writer & Education Consultant
www.mabelfrandsenauthor.example

04739158260
mfrandwrites@quillpost.example

The back has:
Books
The Copperfen Locket Puzzles (In bold)
The Riddle of the Copperfen Locket (in italics)
The Puzzle of the Copperfen (italics)
The Thorncastle Project (in bold)
Book 1: Stuck (italics)
Book 2: Unstuck (italics)

I'm happy for you to change the design provided the 'robin' stays.
Thank you.

Colors
ec2027

Requirements
Must have
• the robin redbreast bird logo - although it is fine to change how the bird looks.
Should not have
• no watermark

```html
<!DOCTYPE html>
<html lang="en">
<head>
<meta charset="utf-8">
<title>Mabel Frandsen — Business Card</title>
<link rel="stylesheet" href="https://fonts.googleapis.com/css2?family=Gelasio:wght@400&family=Alegreya:wght@500&display=swap">
<style>
  :root {
    --backdrop: #4b2f15;
    --card-light: #f3efe9;
    --card-mid: #b2a08a;
    --card-dark: #765e44;
    --card-shadow: rgba(30, 16, 4, 0.6);
    --ink-white: #ffffff;
    --ink-outline: #5a4328;
    --robin-orange: #e8762a;
    --robin-grey: #8f8676;
  }
  * { margin: 0; padding: 0; box-sizing: border-box; }
  html, body { width: 1200px; height: 900px; overflow: hidden; }
  body { background: var(--backdrop); position: relative; }

  .card {
    position: absolute;
    width: 667px;
    height: 408px;
    box-shadow: 4px 5px 6px var(--card-shadow);
  }
  .card--front {
    left: 112px; top: 80px;
    z-index: 2;
    background: radial-gradient(ellipse 420px 300px at 270px 215px, var(--card-light) 0%, var(--card-mid) 45%, var(--card-dark) 100%);
  }
  .card--back {
    left: 463px; top: 380px;
    z-index: 1;
    background: radial-gradient(ellipse 420px 300px at 250px 190px, var(--card-light) 0%, var(--card-mid) 45%, var(--card-dark) 100%);
  }

  .outlined {
    color: var(--ink-white);
    text-shadow:
      -1px -1px 0 var(--ink-outline), 1px -1px 0 var(--ink-outline),
      -1px 1px 0 var(--ink-outline), 1px 1px 0 var(--ink-outline);
  }

  .card__heading {
    position: absolute;
    left: 0; top: 58px; width: 667px;
    text-align: center;
    font-family: "Gelasio", Georgia, serif;
    font-weight: 400;
    line-height: 40px;
  }
  .card__name { font-size: 36px; display: block; transform: translateX(-5px); }
  .card__title { font-size: 37px; display: block; }

  .robin {
    position: absolute;
    left: 395px; top: 138px;
    width: 272px; height: 270px;
    background:
      radial-gradient(ellipse 55px 60px at 140px 95px, var(--robin-orange) 0%, rgba(232,118,42,0) 100%),
      radial-gradient(ellipse 130px 110px at 160px 140px, var(--robin-grey) 0%, rgba(143,134,118,0) 100%);
  }

  .contact {
    position: absolute;
    left: 40px; top: 253px;
    z-index: 1;
    list-style: none;
    font-family: "Gelasio", Georgia, serif;
    font-size: 20px;
  }
  .contact__item {
    display: flex; align-items: center;
    height: 38px; gap: 6px;
  }
  .contact__icon { width: 52px; height: 36px; flex: none; }

  .booklist {
    position: absolute;
    left: 0; top: 128px; width: 690px;
    list-style: none;
    text-align: center;
    font-family: "Alegreya", Georgia, serif;
    font-weight: 500;
    font-size: 28px;
    line-height: 39.5px;
  }
</style>
</head>
<body>

<section class="card card--back">
  <ul class="booklist outlined">
    <li>The Thorncastle Project : Stuck &amp; Unstuck</li>
    <li>The Riddle of the Copperfen Locket</li>
    <li>The Copperfen Locket Puzzles</li>
    <li>The Puzzle of the Copperfen</li>
  </ul>
</section>

<section class="card card--front">
  <h1 class="card__heading outlined">
    <span class="card__name">Mabel Frandsen</span>
    <span class="card__title">Writer &amp; Education Consultant</span>
  </h1>

  <div class="robin" role="img" aria-label="Robin redbreast perched on a branch, singing"></div>

  <ul class="contact outlined">
    <li class="contact__item">
      <svg class="contact__icon" viewBox="0 0 52 36" aria-hidden="true">
        <path d="M2 12 Q26 -2 50 12 L46 16 L38 14 L37 9 Q26 5 15 9 L14 14 L6 16 Z" fill="#fff"/>
        <rect x="10" y="16" width="32" height="18" rx="3" fill="#fff"/>
        <circle cx="26" cy="25" r="6" fill="none" stroke="#765e44" stroke-width="2"/>
      </svg>
      <span>04739158260</span>
    </li>
    <li class="contact__item">
      <svg class="contact__icon" viewBox="0 0 52 36" aria-hidden="true">
        <rect x="2" y="1" width="48" height="34" rx="4" fill="#fff"/>
        <rect x="6" y="9" width="40" height="18" fill="#765e44"/>
        <text x="26" y="22" text-anchor="middle" font-family="Arial, sans-serif" font-size="11" fill="#fff">www.</text>
      </svg>
      <span>mabelfrandsenauthor.example</span>
    </li>
    <li class="contact__item">
      <svg class="contact__icon" viewBox="0 0 52 36" aria-hidden="true">
        <rect x="6" y="0" width="40" height="36" rx="5" fill="#fff"/>
        <rect x="2" y="8" width="8" height="4" rx="2" fill="#fff"/>
        <rect x="2" y="24" width="8" height="4" rx="2" fill="#fff"/>
        <text x="28" y="26" text-anchor="middle" font-family="Arial, sans-serif" font-size="22" fill="#765e44">@</text>
      </svg>
      <span>mfrandwrites@quillpost.example</span>
    </li>
  </ul>
</section>

</body>
</html>
```